Anzeigengestaltung für Hersteller von Material-Prüfmaschinen
Zielgruppe
Wir sind Hersteller von Material-Prüfmaschinen und unsere Maschinen werden in über 20 Branchen eingesetzt. Um Materialkennwerte (was hält z.B. ein Metallstange aus) zu ermitteln, prüfen unsere Kunden ihre Produkte/Materialien auf Zugfestigkeit, Biegefestigkeit, Druckfestigkeit,… Das bedeutet, das Resultat ist immer eine zerstörte Material-Probe, Bauteil,… Zielgruppe sind Bestands- und Neukunden aus dem B2B Umfeld. Mehr Infos www.brenkor-beispiel.de
Aufgabenstellung
- Zentraler Bestandteil der Anzeige soll die zerstörte Probe/Bauteil sein, in welchem sich der Betrachter wieder erkennt. Es soll prominent in Szene gesetzt sein und die Faszination des Zerstörten soll auf den Betrachter wirken.
- Zwingende Bestandteile: Bild der Probe, Logo, Headline (Intelligent Testing Damit es hält was Sie versprechen -> Intelligent Testing kann hier auch abgesetzt oder in einer anderen Schriftart sein)
- Das Motiv muss sowohl mit Motiven die ganz abgebildet sind, als auch mit angeschnittenen Bildern funktionieren
- Hausschrift ist HelveticaNeue, aber nicht zwingend notwendig
- Bild der zerstörten Probe darf bearbeitet werden (Filter, Effekte,…) muss aber noch als solche erkennbar sein
- Im Footer (oder an anderer Stelle) soll noch Platz für ca. 200 Zeichen Text und eine kleine Abbildung der Prüfmaschine (die das Produkt zerstört hat) sein (steadyframe.png), die Anzeige muss aber auch ohne Footer abbildbar sein.
- Anzeige muss im Hoch- und Querformat abbildbar sein

```html
<!DOCTYPE html>
<html lang="de">
<head>
<meta charset="utf-8">
<title>Brenkor Halvek – Intelligent Testing Anzeige</title>
<link rel="stylesheet" href="https://fonts.googleapis.com/css2?family=Inter:wght@300;400;700&display=swap">
<style>
  :root {
    --stage: #b4b4b6;
    --paper: #ffffff;
    --brand-red: #c20e1a;
    --ink: #1d1d1b;
    --sub-grey: #4a4a4a;
    --body-white: #ffffff;
    --photo-light: #e4e6e8;
    --photo-dark: #4a4a4c;
  }
  * { margin: 0; padding: 0; box-sizing: border-box; }
  html, body {
    width: 1200px; height: 675px; overflow: hidden;
    background: var(--stage);
    font-family: "Inter", "Helvetica Neue", Arial, sans-serif;
  }
  .ad {
    position: absolute; left: 122px; top: 0;
    width: 955px; height: 675px;
    background: var(--paper);
    overflow: hidden;
  }
  .ad-art { position: absolute; inset: 0; }
  .brand {
    position: absolute; right: 18px; top: 62px;
    font-weight: 700; font-size: 44px; letter-spacing: -1px;
    color: var(--ink); line-height: 1;
  }
  .headline {
    position: absolute; left: 40px; top: 300px;
    font-weight: 700; font-size: 58px; letter-spacing: -0.5px;
    color: var(--brand-red); line-height: 1;
  }
  .subline {
    position: absolute; left: 41px; top: 370px;
    font-weight: 300; font-size: 32px;
    color: var(--sub-grey); line-height: 1;
  }
  .body-copy {
    position: absolute; left: 39px; top: 489px; width: 636px;
    color: var(--body-white); font-size: 11.6px; line-height: 15px; font-weight: 400;
  }
  .body-copy p + p { margin-top: 15px; }
  .machine {
    position: absolute; left: 760px; top: 328px; width: 170px; height: 334px;
  }
</style>
</head>
<body>
  <main class="ad">
    <svg class="ad-art" width="955" height="675" viewBox="0 0 955 675">
      <defs>
        <linearGradient id="sampleTone" x1="0" y1="1" x2="1" y2="0">
          <stop offset="0" stop-color="var(--photo-light)"/>
          <stop offset="0.5" stop-color="var(--photo-dark)"/>
          <stop offset="1" stop-color="var(--photo-light)"/>
        </linearGradient>
      </defs>
      <polygon role="img" aria-label="Foto einer zerrissenen Faserverbund-Zugprobe mit herausragenden Carbonfasern"
               points="0,135 390,0 760,0 955,250 955,395 720,315 0,382"
               fill="url(#sampleTone)" opacity="0.55"/>
      <polygon class="footer-band" points="0,470 955,382 955,675 0,675" fill="var(--brand-red)"/>
    </svg>

    <div class="brand">Brenkor Halvek</div>

    <h1 class="headline">Intelligent Testing</h1>
    <p class="subline">Damit es hält was Sie versprechen</p>

    <div class="body-copy">
      <p>Lorem ipsum dolor sit amet, consetetur sadipscing elitr, sed diam nonumy eirmod tempor invidunt ut labore et dolore magna aliquyam erat, sed diam voluptua. At vero eos et accusam et justo duo dolores et ea rebum. Stet clita kasd gubergren, no sea takimata sanctus est Lorem ipsum dolor sit amet. Lorem ipsum dolor sit amet, consetetur sadipscing elitr, sed diam nonumy eirmod tempor invidunt ut labore et dolore magna aliquyam erat, sed diam voluptua. At vero eos et accusam et justo duo dolores et ea rebum. Stet clita kasd gubergren, no sea takimata sanctus est Lorem ipsum dolor sit amet. Lorem ipsum dolor sit amet, consetetur sadipscing elitr, sed diam nonumy eirmod tempor invidunt ut labore et dolore magna aliquyam erat, sed diam voluptua. At vero eos et accusam et justo duo dolores et ea rebum. Stet clita kasd gubergren, no sea takimata sanctus est Lorem ipsum dolor sit amet.</p>
      <p>Duis autem vel eum iriure dolor in hendrerit in vulputate velit esse molestie consequat, vel illum dolore eu feugiat nulla facilisis at vero eros et accumsan et iusto odio dignissim qui blandit praesent luptatum zzril delenit augue duis dolore te feugait nulla facilisi. Lorem ipsum dolor sit amet.</p>
    </div>

    <svg class="machine" viewBox="0 0 170 334" role="img" aria-label="Produktfoto der Material-Prüfmaschine steadyframe">
      <defs>
        <linearGradient id="machineTone" x1="0" y1="0" x2="1" y2="0">
          <stop offset="0" stop-color="#8e8a86"/>
          <stop offset="0.5" stop-color="#c9c6c2"/>
          <stop offset="1" stop-color="#7d7974"/>
        </linearGradient>
      </defs>
      <rect x="0" y="0" width="170" height="334" rx="4" fill="url(#machineTone)"/>
    </svg>
  </main>
</body>
</html>
```